Global Aviation Services website

we are a start up airline/aviation services company that will operate in Australia, USA and New Zealand initially. Fundamentally the service is to airlines who fly into and out of a market yet do not wish to have their own admin, sales and marketing infrastructures. They would use us.
The company name is Veltaro.
It needs to look sophisticated, sharp and professional. We would like it designed and built in the CMS - wordpress so we can update after the project is finished when necessary. An example of who we are and a good website we like can be found at: http://pembrikegroup.example/. There is no ecommerce or interactivity other than a contact us. We do like animation for promotion. There will be links to our airline clients and sub sites or pages will exist for the various offices we have globally. Currently 6. Each of these offices will have a dedicated local URL. Please submit your suggestion of a home page and 2 internal pages. Thank you and kind regards Miriam
Target Market(s)
airlines, airline technology companies,
Industry/Entity Type
Aviation
Coding
Coded - Design and coding required
Number of Pages Required
5+ page
Look and feel

```html
<!DOCTYPE html>
<html lang="en">
<head>
<meta charset="utf-8">
<title>Veltaro — Start Up Airline</title>
<link href="https://fonts.googleapis.com/css2?family=Open+Sans:wght@400;600&family=Raleway:wght@300;400;500&display=swap" rel="stylesheet">
<style>
:root{
  --blue:#0b57a6;
  --blue-deep:#0a4a8e;
  --blue-dark:#08396f;
  --red:#e42529;
  --ink:#222;
  --body:#444;
  --muted:#8a8a8a;
  --grey-bg:#f3f3f3;
  --line:#d8d8d8;
  --white:#fff;
}
*{box-sizing:border-box;margin:0;padding:0}
html,body{width:1200px;height:2489px;overflow:hidden}
body{position:relative;background:var(--white);font-family:"Open Sans",sans-serif;color:var(--body)}
.abs{position:absolute}
.nowrap{white-space:nowrap}
h1,h2,h3{font-family:"Raleway",sans-serif;font-weight:400;color:var(--ink)}
.btn{position:absolute;display:flex;align-items:center;justify-content:center;border-radius:20px;font-size:13px;font-family:"Open Sans",sans-serif}
.btn-outline{border:2px solid var(--blue);color:var(--blue);background:transparent;font-size:13.5px}

/* header */
.site-header{left:0;top:0;width:1200px;height:62px;background:var(--white);border-bottom:1px solid #e6e6e6}
.logo{left:100px;top:12px;font-family:"Raleway",sans-serif;font-weight:500;font-size:32px;color:var(--blue-dark);letter-spacing:1px}
.nav{left:527px;top:0;display:flex;height:62px}
.nav a{display:block;padding:22px 16px 0;font-size:13px;color:var(--ink);text-decoration:none;height:62px}
.nav a.active{color:var(--blue);border-top:3px solid var(--blue);padding-top:19px}
.search{left:1075px;top:14px;width:35px;height:35px;border-radius:50%;background:var(--red)}

/* hero */
.hero{left:0;top:62px;width:1200px;height:435px;background:var(--grey-bg)}
.hero-title{left:0;top:143px;width:1200px;text-align:center;font-size:46px;font-weight:500}
.hero-sub{left:0;top:203px;width:1200px;text-align:center;font-family:"Raleway",sans-serif;font-size:19px;color:var(--muted);font-weight:300}
.hero-illus{left:327px;top:328px;width:546px;height:196px;border-radius:8px 8px 40% 40%/8px 8px 20px 20px;background:linear-gradient(180deg,#dfe5ef 0%,#9fb4d3 60%,#1f5ea8 100%)}

/* who */
.who{left:0;top:497px;width:1200px;height:223px;background:var(--blue)}
.who h2{position:absolute;left:0;top:52px;width:1200px;text-align:center;color:var(--white);font-size:26px}
.who p{position:absolute;left:0;top:88px;width:1200px;text-align:center;color:var(--white);font-size:13px;line-height:20px;white-space:nowrap}
.who .btn{border:2px solid var(--white);color:var(--white);left:531px;top:145px;width:139px;height:38px;font-size:13.5px}

/* what */
.what-img{left:110px;top:760px;width:355px;height:246px;background:linear-gradient(160deg,#8096bf 0%,#cdd3e1 50%,#c26a30 100%)}
.sec-h{font-size:32px}
.sec-p{font-size:13px;line-height:19.5px;color:var(--body);white-space:nowrap}

/* clients */
.clients{left:0;top:1040px;width:1200px;height:302px;background:var(--grey-bg)}
.clients-frame{left:740px;top:1076px;width:321px;height:293px;background:var(--white)}
.clients-img{left:745px;top:1081px;width:309px;height:287px;background:linear-gradient(180deg,#1e4fa0 0%,#6b7487 45%,#5a3a30 100%)}

/* news */
.news-photo{width:222px;height:220px}
.news-frame{border:1px solid rgba(255,255,255,.7)}
.news-card{width:268px;height:249px;background:var(--white);border:1px solid var(--line)}
.news-card h3{position:absolute;left:31px;top:36px;font-size:18px}
.news-card .dash{position:absolute;left:31px;top:63px;width:14px;height:2px;background:#2e8b3e}
.news-card p{position:absolute;left:31px;top:77px;font-size:11px;line-height:17.5px;color:var(--body);white-space:nowrap}
.news-card .btn{left:32px;top:178px;width:104px;height:35px;font-size:13px}
.date-num{width:84px;height:50px;background:var(--blue);color:var(--white);font-family:"Raleway",sans-serif;font-size:38px;text-align:right;padding-right:14px;line-height:50px;clip-path:polygon(30% 0,100% 0,100% 100%,0 100%)}
.date-mon{width:62px;height:27px;background:#111;color:var(--white);font-size:12px;line-height:27px;text-align:right;padding-right:14px}

/* contact */
.contact{left:0;top:1758px;width:1200px;height:478px;background:var(--grey-bg)}
.tab{height:38px;border:2px solid var(--blue);border-radius:20px;color:var(--blue);font-size:13px;display:flex;align-items:center;justify-content:center;position:absolute}
.map{left:89px;top:1918px;width:476px;height:256px;background:linear-gradient(135deg,#e4e4e4,#cfcfcf)}
.field{background:var(--white);border:1px solid #dcdcdc;font-size:11px;color:var(--muted);padding:15px 15px}

/* footer */
.footer{left:0;top:2236px;width:1200px;height:202px;background:var(--blue)}
.foot-logo{left:89px;top:2307px;font-family:"Raleway",sans-serif;font-weight:500;font-size:40px;color:var(--white);letter-spacing:1px}
.foot-col h4{font-family:"Open Sans",sans-serif;font-weight:600;font-size:14.5px;color:var(--white);margin-bottom:8px}
.foot-col li{list-style:none;font-size:11.5px;color:var(--white);line-height:21.5px}
.social{width:38px;height:38px;border-radius:50%}
.bottom-bar{left:0;top:2438px;width:1200px;height:51px;background:var(--blue-dark);color:var(--white);font-size:12.5px}
</style>
</head>
<body>

<header class="abs site-header"></header>
<div class="abs logo">Veltaro</div>
<nav class="abs nav">
  <a class="active">Who we are</a><a>What we do</a><a>Our clients</a><a>What's happening</a><a>Contact us</a>
</nav>
<div class="abs search">
  <svg width="35" height="35" viewBox="0 0 35 35"><circle cx="16" cy="16" r="5" fill="none" stroke="#fff" stroke-width="2"/><line x1="19.6" y1="19.6" x2="23" y2="23" stroke="#fff" stroke-width="2" stroke-linecap="round"/></svg>
</div>

<section class="abs hero"></section>
<h1 class="abs hero-title">Start Up Airline</h1>
<div class="abs hero-sub">Aviation services company</div>
<div class="btn" style="left:463px;top:243px;width:131px;height:38px;background:var(--blue);color:#fff">LEARN MORE</div>
<div class="btn" style="left:602px;top:243px;width:130px;height:38px;background:var(--red);color:#fff">CONTACT US</div>
<div class="abs hero-illus" role="img" aria-label="Travel illustration: suitcase, clock tower, Eiffel tower, hotel, camera and passport"></div>

<section class="abs who">
  <h2>Who we are</h2>
  <p>Lorem ipsum dolor sit amet, consectetuer adipiscing elit. Aenean commodo ligula eget dolor. Aenean massa. Cum sociis natoque penatibus<br>et magnis dis parturient montes, nascetur ridiculus mus donec quam felis ultricies nec pellentesque eu.</p>
  <div class="btn">Find out more</div>
</section>

<div class="abs what-img" role="img" aria-label="Photo of a passenger jet landing at sunset"></div>
<h2 class="abs sec-h" style="left:516px;top:768px">What we do</h2>
<p class="abs sec-p" style="left:519px;top:807px">Lorem ipsum dolor sit amet, consectetuer adipiscing elit. Aenean commodo ligula eget dolor.<br>Aenean massa. Cum sociis natoque penatibus et magnis dis parturient montes, nascetur<br>ridiculus mus. Donec quam felis, ultricies nec, pellentesque eu, pretium quis, sem. Nulla<br>consequat massa quis enim.</p>
<p class="abs sec-p" style="left:519px;top:895px">Aenean commodo ligula eget dolor. Aenean massa. Cum sociis natoque penatibus et magnis<br>dis parturient montes, nascetur</p>
<div class="btn btn-outline" style="left:521px;top:949px;width:139px;height:37px">Find out more</div>

<section class="abs clients"></section>
<h2 class="abs sec-h" style="left:0;top:1093px;width:666px;text-align:right">Our clients</h2>
<p class="abs sec-p" style="left:0;top:1136px;width:668px;text-align:right">Lorem ipsum dolor sit amet, consectetuer adipiscing elit. Aenean commodo ligula eget dolor<br>aenean massa Cum sociis natoque penatibus et magnis dis parturient montes, nascetur<br>. Donec quam felis, ultricies nec, pellentesque eu, pretium quis, sem</p>
<p class="abs sec-p" style="left:0;top:1204px;width:666px;text-align:right">Lorem ipsum dolor sit amet, consectetuer adipiscing elit. Aenean commodo ligula eget dolor<br>.aenean massa Cum sociis natoque penatibus</p>
<div class="btn btn-outline" style="left:530px;top:1259px;width:139px;height:37px">Find out more</div>
<div class="abs clients-frame"></div>
<div class="abs clients-img" role="img" aria-label="Busy airport terminal with departure boards above travellers"></div>

<h2 class="abs" style="left:86px;top:1391px;font-size:31px">Latest News</h2>

<div class="abs news-photo" style="left:89px;top:1464px;background:linear-gradient(160deg,#5a3a2a 0%,#e7a24b 45%,#2a2420 100%)" role="img" aria-label="Traveller with headphones looking out of a plane window at sunset"></div>
<div class="abs news-frame" style="left:104px;top:1480px;width:207px;height:188px"></div>
<div class="abs date-num" style="left:225px;top:1538px">10</div>
<div class="abs date-mon" style="left:248px;top:1595px">Feb</div>
<article class="abs news-card" style="left:309px;top:1449px">
  <h3>News Heading 1</h3><span class="dash"></span>
  <p>Lorem ipsum dolor sit amet, consectetuer<br>adipiscing elit. Aenean commodo ligula<br>eget dolor. Cum sociis natoque penatibus<br>et magnis Lorem ipsum dolor sit amet,<br>consectetuer adipiscing elit.</p>
  <div class="btn btn-outline">Read More</div>
</article>

<div class="abs news-photo" style="left:622px;top:1464px;background:linear-gradient(160deg,#9aa0a4 0%,#b2553a 50%,#3a342e 100%)" role="img" aria-label="Traveller with backpack walking through an airport concourse"></div>
<div class="abs news-frame" style="left:637px;top:1480px;width:207px;height:188px"></div>
<div class="abs date-num" style="left:758px;top:1538px">10</div>
<div class="abs date-mon" style="left:781px;top:1595px">Feb</div>
<article class="abs news-card" style="left:842px;top:1449px">
  <h3>News Heading 2</h3><span class="dash"></span>
  <p>Lorem ipsum dolor sit amet, consectetuer<br>adipiscing elit. Aenean commodo ligula<br>eget dolor. Cum sociis natoque penatibus<br>et magnis Lorem ipsum dolor sit amet,<br>consectetuer adipiscing elit.</p>
  <div class="btn btn-outline">Read More</div>
</article>

<section class="abs contact"></section>
<h2 class="abs" style="left:0;top:1800px;width:1200px;text-align:center;font-size:31px">Contact Us</h2>
<div class="tab" style="left:418px;top:1855px;width:111px">Australia</div>
<div class="tab" style="left:535px;top:1855px;width:110px">USA</div>
<div class="tab" style="left:651px;top:1855px;width:120px">New Zealand</div>
<div class="abs map" role="img" aria-label="Street map of the office location with a red marker"></div>
<div class="abs field" style="left:600px;top:1918px;width:243px;height:45px">Name*</div>
<div class="abs field" style="left:849px;top:1918px;width:243px;height:45px">Email*</div>
<div class="abs field" style="left:600px;top:1968px;width:492px;height:152px">Message*</div>
<div class="btn btn-outline" style="left:600px;top:2135px;width:110px;height:38px">Submit</div>

<footer class="abs footer"></footer>
<div class="abs foot-logo">Veltaro</div>
<div class="abs foot-col" style="left:397px;top:2264px">
  <h4>NEED HELP?</h4>
  <ul><li style="line-height:25px">Email Us</li><li style="line-height:25px">Talk To Us</li><li style="line-height:25px">Tweet Us</li><li style="line-height:25px">Login Help</li></ul>
</div>
<div class="abs foot-col" style="left:625px;top:2264px">
  <h4>USEFUL LINKS</h4>
  <ul><li>Who we are</li><li>What we do</li><li>Our clients</li><li>What's happening</li><li>Contact us</li></ul>
</div>
<div class="abs foot-col" style="left:855px;top:2264px"><h4>CONNECT WITH US</h4></div>
<div class="abs social" style="left:854px;top:2299px;background:#3a6cc4" role="img" aria-label="Social profile link"></div>
<div class="abs social" style="left:899px;top:2299px;background:#2cb7ef" role="img" aria-label="Social profile link"></div>
<div class="abs social" style="left:944px;top:2299px;background:#d8342c" role="img" aria-label="Social profile link"></div>
<div class="abs social" style="left:989px;top:2299px;background:#0f4c8a" role="img" aria-label="Social profile link"></div>

<div class="abs bottom-bar">
  <span class="abs" style="left:89px;top:17px">Copyright@2016 | All Right Reserved</span>
  <span class="abs" style="right:89px;top:17px">Travel may be on other airlines.</span>
</div>

</body>
</html>
```